Cover design required for our new homes catalogue

Kestrel Homes build new prefabricated homes in New Zealand.
Our smart building system means we can supply houses at affordable prices and deliver them all over New Zealand.
The catalogue content tells customers about our company and shows them our range of house designs.
The cover needs to be inviting and professional.
Our main company colour is Pantone Blue 3005.
Secondary colours are Pantone dark blue 302 & Grey (40% black).

I'll upload a copy of our old catalogue cover & some new pictures - we want a different layout but similar content, just new pictures.

Target Market(s)

Professional people wanting a new home, holiday home, farm home, rural homes, small homes, prefabricated office buildings, tourist accommodation

Industry/Entity Type

Residential Construction

Font styles to use
Sans Serif

Colors
0692cd

Requirements
Must have
• Our logo & Tagline "Smart affordable homes".
Nice to have
• Pictures of our homes & scenery

```html
<!DOCTYPE html>
<html lang="en">
<head>
<meta charset="utf-8">
<title>Kestrel Homes – Homes Catalogue Cover</title>
<link rel="stylesheet" href="https://fonts.googleapis.com/css2?family=Open+Sans:wght@400;600;700&display=swap">
<style>
  :root {
    --brand-blue: #0692cd;
    --dark-blue: #263a8f;
    --mid-blue: #0d73bd;
    --tile-blue: #0b86cf;
    --grey: #8f8f8f;
    --paper-top: #e9eef2;
    --paper-mid: #a9d3e9;
    --backdrop: #eceff1;
    --white: #ffffff;
  }
  * { margin: 0; padding: 0; box-sizing: border-box; }
  html, body { width: 1200px; height: 804px; overflow: hidden; }
  body {
    background: var(--backdrop);
    font-family: "Open Sans", Arial, sans-serif;
    position: relative;
  }
  .cover {
    position: absolute;
    left: 330px;
    top: 20px;
    width: 540px;
    height: 764px;
    background: linear-gradient(180deg, var(--paper-top) 0%, var(--paper-mid) 40%, var(--brand-blue) 100%);
    box-shadow: 0 6px 24px rgba(0,0,0,0.18);
    display: flex;
    flex-direction: column;
    align-items: center;
  }
  .brand {
    margin-top: 78px;
    display: flex;
    flex-direction: column;
    align-items: center;
  }
  .brand-square {
    width: 48px;
    height: 48px;
    background: var(--brand-blue);
  }
  .brand-name {
    margin-top: 14px;
    font-weight: 600;
    font-size: 20px;
    line-height: 1.2;
    letter-spacing: 0.5px;
    text-transform: uppercase;
    color: var(--brand-blue);
  }
  .tagline {
    margin-top: 4px;
    font-weight: 400;
    font-size: 12px;
    line-height: 1.2;
    letter-spacing: 1px;
    color: var(--grey);
  }
  .photo-grid {
    margin-top: 28px;
    display: grid;
    grid-template-columns: repeat(3, 116px);
    grid-template-rows: repeat(3, 116px);
    gap: 8px;
  }
  .tile { width: 116px; height: 116px; }
  .tile--blue { background: var(--tile-blue); }
  .tile--mid { background: var(--mid-blue); }
  .tile--dark { background: var(--dark-blue); }
  .photo--landscape { background: linear-gradient(180deg, #6f95bd 0%, #8a8170 50%, #a38b63 100%); }
  .photo--transport { background: linear-gradient(180deg, #b8c9d6 0%, #7f7f7a 55%, #5f7b5a 100%); }
  .photo--house { background: linear-gradient(180deg, #8fb2d6 0%, #8c8479 55%, #9d9270 100%); }
  .photo--bedroom { background: linear-gradient(180deg, #c9b495 0%, #8a6e4d 60%, #d8d0c4 100%); }
  .photo--deck { background: linear-gradient(160deg, #f2d58e 0%, #9c6a34 55%, #5a3a1e 100%); }
  .photo--kitchen { background: linear-gradient(180deg, #e6e8ea 0%, #cfd3d6 60%, #9a9ea2 100%); }
  .title {
    margin-top: 56px;
    font-weight: 400;
    font-size: 31px;
    line-height: 1.2;
    letter-spacing: 1px;
    color: var(--white);
    text-transform: uppercase;
  }
  .website {
    margin-top: 22px;
    font-size: 11px;
    letter-spacing: 1px;
    color: rgba(255,255,255,0.6);
  }
</style>
</head>
<body>
  <main class="cover">
    <header class="brand">
      <div class="brand-square"></div>
      <div class="brand-name">Kestrel Homes</div>
      <p class="tagline">Smart affordable homes</p>
    </header>

    <section class="photo-grid">
      <div class="tile photo--landscape" role="img" aria-label="Mountain tussock landscape under blue sky"></div>
      <div class="tile photo--transport" role="img" aria-label="Prefabricated house being delivered on a truck"></div>
      <div class="tile tile--blue"></div>
      <div class="tile tile--mid"></div>
      <div class="tile photo--house" role="img" aria-label="Completed single-storey home in rural setting"></div>
      <div class="tile photo--bedroom" role="img" aria-label="Warmly lit bedroom interior"></div>
      <div class="tile photo--deck" role="img" aria-label="Timber deck with outdoor chair at sunset"></div>
      <div class="tile photo--kitchen" role="img" aria-label="Modern white kitchen with bench stools"></div>
      <div class="tile tile--dark"></div>
    </section>

    <h1 class="title">Homes Catalogue</h1>
    <p class="website">www.kestrelhomes.example</p>
  </main>
</body>
</html>
```